Meridale painting

We are a Painting company. We paint residential and commercial, interior& exterior painting, cabinets refinish,acoustic ceiling painting,popcorn ceiling removal,drywall repair,iron and concrete painting

We don't have any Facebook page or website.

We are a Painting company. We paint residential and commercial, interior& exterior painting, cabinets refinish,acoustic ceiling painting,popcorn ceiling removal,drywall repair,iron and concrete painting We don't have any Facebook page or website.

Requirements
Must have
• I need 200 cards. 50 of with my name Tobin, 50 with Owen 50 with Harold qnd 50 with bastian

```html
<!DOCTYPE html>
<html lang="en">
<head>
<meta charset="utf-8">
<title>Meridale Painting – Business Card</title>
<link href="https://fonts.googleapis.com/css2?family=Montserrat:wght@500;600;700;800&family=Roboto+Condensed:wght@700&display=swap" rel="stylesheet">
<style>
  :root{
    --backdrop:#2b2b2d;
    --paper:#ffffff;
    --purple:#6e2a88;
    --purple-deep:#5a1f72;
    --magenta:#d63c91;
    --orange:#f07a2a;
    --amber:#f5a623;
    --sun:#fbd27a;
    --yellow:#fff200;
    --ink:#5a1f72;
  }
  *{box-sizing:border-box;margin:0;padding:0}
  html,body{width:1200px;height:900px;overflow:hidden}
  body{background:var(--backdrop);font-family:"Montserrat",sans-serif;position:relative}

  .card{position:absolute;width:640px;height:365px;left:280px;background:var(--paper);border-radius:22px;overflow:hidden}
  .card--front{top:55px}
  .card--back{top:475px}

  /* front artwork area */
  .art-front{position:absolute;left:40px;top:18px;right:30px;bottom:18px;
    background:linear-gradient(100deg,var(--purple) 0%,var(--purple) 50%,var(--orange) 78%,var(--sun) 100%);
    clip-path:polygon(8% 20%,40% 0,100% 0,100% 80%,70% 100%,10% 100%,0 70%)}
  .brand-band{position:absolute;left:110px;top:158px;display:flex;align-items:center}
  .brand-mark{width:56px;height:56px;background:var(--amber)}
  .brand-name{background:var(--purple-deep);color:var(--paper);font-weight:700;font-size:30px;letter-spacing:2px;text-transform:uppercase;padding:8px 22px;height:48px;line-height:32px}

  /* back artwork area */
  .art-back{position:absolute;left:0;top:0;width:380px;height:365px;
    background:linear-gradient(60deg,var(--purple) 0%,var(--magenta) 35%,var(--orange) 65%,var(--sun) 95%);
    clip-path:polygon(0 20%,45% 5%,85% 0,100% 45%,80% 90%,60% 100%,0 100%)}
  .tag{position:absolute;color:var(--paper);font-family:"Roboto Condensed",sans-serif;font-weight:700;font-size:15px;letter-spacing:.5px;text-transform:uppercase;padding:6px 14px}
  .tag--sector{left:40px;bottom:36px;background:var(--magenta)}
  .tag--scope{right:44px;bottom:88px;background:var(--orange)}

  .contact{position:absolute;right:40px;top:30px;width:280px;text-align:right}
  .contact__name{font-size:24px;font-weight:800;letter-spacing:1.5px;text-transform:uppercase;color:var(--orange)}
  .contact__name span{color:var(--ink)}
  .contact__line{display:flex;justify-content:flex-end;align-items:center;gap:8px;color:var(--ink)}
  .contact__phone{font-size:19px;font-weight:700;margin-top:4px}
  .contact__email{font-size:12px;font-weight:500;margin-top:2px}
  .contact__rule{height:2px;background:var(--orange);margin:8px 0 10px 0}
  .icon{width:14px;height:14px;flex:none}

  .services{list-style:none;font-size:13px;font-weight:500;color:var(--ink);line-height:1.55}
  .services li{display:flex;justify-content:flex-end;align-items:center;gap:8px}
  .services li::after{content:"";width:8px;height:8px;border-radius:2px;background:var(--orange);flex:none}
  .services li:nth-child(2)::after{background:var(--magenta)}
  .services li:nth-child(3)::after{background:var(--amber)}
  .services li:nth-child(4)::after{background:var(--magenta)}
  .services li:nth-child(5)::after{background:var(--purple)}
</style>
</head>
<body>

<section class="card card--front" aria-label="Card front">
  <div class="art-front" role="img" aria-label="Paint splash artwork in purple, pink, orange and yellow"></div>
  <div class="brand-band">
    <div class="brand-mark"></div>
    <div class="brand-name">Meridale Painting</div>
  </div>
</section>

<section class="card card--back" aria-label="Card back">
  <div class="art-back" role="img" aria-label="Paint splash artwork in purple, pink, orange and yellow"></div>
  <div class="tag tag--sector">Residential and Commercial</div>

  <div class="contact">
    <div class="contact__name">Tobin <span>Marsh</span></div>
    <div class="contact__line contact__phone">555-0142-318
      <svg class="icon" viewBox="0 0 24 24" aria-hidden="true"><path fill="#f07a2a" d="M6.6 10.8a15 15 0 0 0 6.6 6.6l2.2-2.2a1 1 0 0 1 1-.25 11.4 11.4 0 0 0 3.6.57 1 1 0 0 1 1 1V20a1 1 0 0 1-1 1A17 17 0 0 1 3 4a1 1 0 0 1 1-1h3.5a1 1 0 0 1 1 1c0 1.25.2 2.45.57 3.57a1 1 0 0 1-.25 1z"/></svg>
    </div>
    <div class="contact__line contact__email">meridalepainting@inbox.net
      <svg class="icon" viewBox="0 0 24 24" aria-hidden="true"><rect x="2" y="5" width="20" height="14" rx="1" fill="#f07a2a"/><path d="M2 6l10 7 10-7" fill="none" stroke="#fff" stroke-width="1.8"/></svg>
    </div>
    <div class="contact__rule"></div>
    <ul class="services">
      <li>Cabinets refinish</li>
      <li>Acoustic ceiling painting</li>
      <li>Popcorn ceiling removal</li>
      <li>drywall repair</li>
      <li>Iron and concrete painting</li>
    </ul>
  </div>

  <div class="tag tag--scope">Interior &amp; Exterior Painting</div>
</section>

</body>
</html>
```